Landing Page Design für Tor- und Zaunbaufirma
Zielgruppe
der Kunde ist eine Tor- und Zaunbaufirma. Die Zielgruppen sind private Häuslebauer und Firmen.
Aufgabenstellung
Die Farben des Logos sollen nur sehr sparsam eingesetzt werden.
Die Navigation soll sich an der jetzigen Webseite orientieren. www.frenk-gitterwerk.de
Impressum und Datenschutz dezenter platzieren
Kommunikationsdaten vordergründig darstellen
mehr als 25-Jahre Erfahrung im Tor- und Zaunbau
Regionalität beachten

```html
<!DOCTYPE html>
<html lang="de">
<head>
<meta charset="utf-8">
<title>Tor &amp; Zaunbau Frenk</title>
<link href="https://fonts.googleapis.com/css2?family=Nunito:ital,wght@0,700;1,700&display=swap" rel="stylesheet">
<style>
:root{
  --magenta:#ec008c;
  --coral:#fc6c67;
  --blue:#2b8ae6;
  --sky:#3bb8ea;
  --navy:#2d3591;
  --violet:#7358f0;
  --cyan:#2ec8d8;
  --red:#e0303e;
}
*{margin:0;padding:0;box-sizing:border-box}
html,body{width:1200px;height:675px;overflow:hidden;background:#fff}
body{position:relative;font-family:"Nunito",sans-serif;font-style:italic;font-weight:700}
.brand{position:absolute;left:75px;top:34px;display:flex;align-items:center;gap:8px;font-style:normal;font-weight:700;color:var(--magenta);font-size:16px;line-height:1}
.brand-mark{width:14px;height:14px;background:var(--magenta)}
.contact{position:absolute;left:304px;top:14px;color:var(--magenta);font-size:22px;line-height:26.5px;letter-spacing:.3px}
.privacy{position:absolute;left:1081px;top:8px;font-size:8px;color:var(--blue)}
.tagline{position:absolute;right:57px;top:30px;font-size:21px;color:var(--sky);letter-spacing:.3px}
.tagline b{font-size:33px;font-weight:700}
.nav{position:absolute;left:0;top:101px;width:1200px;height:80px;background:linear-gradient(90deg,var(--magenta) 0%,var(--magenta) 38%,var(--coral) 72%,var(--coral) 100%)}
.nav a{position:absolute;top:27px;color:#fff;font-size:21px;text-decoration:none;letter-spacing:.3px}
.carousel{position:absolute;left:0;top:0}
.tile{position:absolute;top:257px;width:211px;height:124px}
.tile-label{position:absolute;top:384px;width:211px;text-align:center;color:#fff;font-size:20px;letter-spacing:.3px}
h1{position:absolute;top:468px;width:1200px;text-align:center;font-weight:700;font-size:39px;color:var(--blue);letter-spacing:.3px}
.sub{position:absolute;top:528px;width:1200px;text-align:center;font-size:27px;line-height:33px;color:var(--blue)}
.intro{position:absolute;top:617px;left:150px;width:900px;text-align:center;font-size:11.5px;line-height:14.5px;color:var(--blue)}
</style>
</head>
<body>
<div class="brand"><span class="brand-mark"></span><span>Tor &amp; Zaunbau Frenk</span></div>
<div class="contact">0371 / 845 17 92<br>0172 / 633 21 09<br>info@frenk-gitterwerk.de</div>
<a class="privacy">Datenschutz</a>
<div class="tagline">Mehr als <b>25</b> Jahre im Tor- und Zaunbau!</div>

<nav class="nav">
  <a style="left:302px">Über Uns</a>
  <a style="left:460px">Unsere Leistungen</a>
  <a style="left:720px">Kontakt</a>
  <a style="left:861px">Impressum</a>
</nav>

<svg class="carousel" width="1200" height="675" viewBox="0 0 1200 675">
  <defs>
    <linearGradient id="band" x1="0" x2="1" y1="0" y2="0">
      <stop offset="0" stop-color="#2d3591"/>
      <stop offset="0.65" stop-color="#7358f0"/>
      <stop offset="1" stop-color="#2ec8d8"/>
    </linearGradient>
  </defs>
  <path d="M224 217 H977 Q1071 250 1071 320 Q1071 390 977 421 H224 Q129 390 129 320 Q129 250 224 217 Z" fill="url(#band)"/>
  <polygon points="222,275 222,363 177,319" fill="var(--red)"/>
  <polygon points="979,275 979,363 1023,319" fill="var(--red)"/>
</svg>

<div class="tile" style="left:247px;background:linear-gradient(#6c6e70,#55575a 80%,#5d8a3a)" role="img" aria-label="Foto einer grauen Sichtschutzanlage"></div>
<div class="tile" style="left:495px;background:linear-gradient(#3f6b34,#b2672c 60%,#4d8a33)" role="img" aria-label="Foto eines Holzzauns im Garten"></div>
<div class="tile" style="left:743px;background:linear-gradient(#2f4a2c,#4b5a4a 60%,#9da0a3)" role="img" aria-label="Foto eines Metallzauns"></div>
<div class="tile-label" style="left:248px">Sichtschutzanlagen</div>
<div class="tile-label" style="left:495px">Holzzäune</div>
<div class="tile-label" style="left:743px">Metallzäune</div>

<h1>Tor &amp; Zaunbau Frenk aus Chemnitz</h1>
<p class="sub">Ihr Partner für alle Zaun- und Torsysteme<br>in den Regionen Chemnitz und Zwickau.</p>
<p class="intro">Wenn es um Zäune, Toranlagen, Schranken geht, ob als Objektschutz für Industrieanlagen, als Lärmschutz für öffentliche Einrichtungen oder ganz einfach als Schmuck und Schutz vor Einblicken im Privatbereich – bei Tor &amp; Zaunbau Frenk können Sie sich auf einen Rund-Um-Service verlassen.</p>
</body>
</html>
```